Stationary Design (using existing logo)

Stationary (print and electronic version for Word/email), envelope, and fax cover. All companies are part of same family or course so designs can be the same, or essentially the same. Use the logos attached, same font and colors.

Target Market(s)

Real estate professionals. Investors and other property owners. Financial professionals.

Industry/Entity Type

Real Estate

Font styles to use
Serif

Requirements
Must have
• Should be a serious, sophisticated design in colors that match the business cards we uploaded. Design needs to match the color and fonts in the attached business cards. Can use the same design for each company, just change logo and color.
Should not have
• Nothing quirky or cute.

```html
<!DOCTYPE html>
<html lang="en">
<head>
<meta charset="utf-8">
<title>Meridane Realty Group – Stationery Set</title>
<link rel="stylesheet" href="https://fonts.googleapis.com/css2?family=Tinos:wght@400;700&display=swap">
<style>
:root{
  --backdrop:#7d7d7d;
  --paper:#ffffff;
  --paper-shade:#f7f7f7;
  --navy:#1a3a80;
  --band:#173a82;
  --ink:#444a55;
  --ink-soft:#6b6f76;
  --field:#e9eaec;
  --faint:#eef0f2;
  --card-grey:#e4e5e7;
  --card-mark:#c9cbce;
}
*{box-sizing:border-box;margin:0;padding:0}
html,body{width:1200px;height:625px;overflow:hidden}
body{background:var(--backdrop);font-family:"Tinos","Times New Roman",serif;color:var(--ink);position:relative}

.sheet{position:absolute;background:linear-gradient(180deg,var(--paper),var(--paper-shade));box-shadow:0 1px 3px rgba(0,0,0,.25);overflow:hidden}
.letterhead{left:62px;top:51px;width:376px;height:531px}
.fax-cover{left:454px;top:51px;width:376px;height:531px}

.brand{position:absolute;text-align:center;color:var(--navy);line-height:1}
.brand-name{display:block;font-size:15px;letter-spacing:.5px;border-bottom:1px solid var(--navy);padding-bottom:1px}
.brand-sub{display:block;font-size:5.5px;letter-spacing:1px;margin-top:2px}
.sheet .brand{left:27px;top:45px;width:94px}

.contact{position:absolute;left:273px;top:30px;font-size:8px;line-height:11px;color:var(--ink-soft);white-space:nowrap}

.watermark{position:absolute;color:var(--faint);font-size:56px;letter-spacing:2px;line-height:1;white-space:nowrap}
.letterhead .watermark{left:40px;top:245px}
.fax-cover .watermark{left:40px;top:330px}

.address-band{position:absolute;left:0;right:0;bottom:0;height:15px;background:var(--band);color:#fff;font-size:7.5px;line-height:15px;text-align:center;white-space:nowrap}

.fax-fields{position:absolute;left:25px;top:94px;display:grid;grid-template-columns:43px 115px 44px 116px;gap:2px 3px;font-size:6.5px}
.fax-fields span{height:16px;background:var(--field);line-height:16px;padding-left:7px;color:var(--ink)}
.fax-options{position:absolute;left:26px;top:170px;width:330px;display:flex;justify-content:space-between;font-size:5.5px;color:var(--ink)}
.fax-options label{display:flex;align-items:center;gap:4px;white-space:nowrap}
.fax-options i{width:7px;height:7px;border:1px solid #777;display:inline-block}
.fax-comments{position:absolute;left:28px;top:187px;font-size:7px;color:var(--ink)}

.card{position:absolute;left:910px;width:173px;height:90px;box-shadow:0 1px 3px rgba(0,0,0,.3);overflow:hidden}
.card-front{top:60px;background:var(--paper)}
.card-front .brand{left:32px;top:12px;width:110px}
.card-front .brand-name{font-size:17px}
.card-person{position:absolute;left:12px;top:57px;font-size:5px;line-height:6px;color:var(--ink);white-space:nowrap}
.card-phones{position:absolute;right:12px;top:62px;font-size:5px;line-height:6px;color:var(--ink);white-space:nowrap}
.card-band{position:absolute;left:0;right:0;bottom:0;height:12px;background:var(--band);color:#fff;font-size:5.5px;line-height:12px;text-align:center;white-space:nowrap}
.card-back{top:165px;background:var(--card-grey)}
.card-back-name{position:absolute;left:14px;top:58px;font-size:13px;line-height:1;letter-spacing:.5px;color:var(--card-mark);white-space:nowrap}
.card-url{position:absolute;left:91px;top:40px;font-size:5.5px;color:var(--ink);white-space:nowrap}

.envelope{position:absolute;left:842px;width:307px;background:var(--paper);box-shadow:0 1px 3px rgba(0,0,0,.25);overflow:hidden}
.envelope-front{top:295px;height:137px}
.envelope-front .brand{left:16px;top:20px;width:70px}
.envelope-front .brand-name{font-size:11.5px}
.envelope-front .brand-sub{font-size:4.5px}
.envelope-front .watermark{left:150px;top:58px;font-size:24px;letter-spacing:1px}
.envelope-front .address-band{height:12px;line-height:12px;font-size:5.5px;bottom:18px}
.envelope-back{top:446px;height:135px}
.envelope-back svg{position:absolute;inset:0}
.envelope-url{position:absolute;left:0;right:0;top:38px;text-align:center;font-size:7px;color:var(--ink)}
.envelope-mark{position:absolute;left:148px;top:25px;width:9px;height:9px;background:#b9bcc0}
</style>
</head>
<body>

<section class="sheet letterhead">
  <div class="brand"><span class="brand-name">MERIDANE</span><span class="brand-sub">REALTY GROUP LLC</span></div>
  <div class="contact">312.555.0146<br>312.555.0147 (fax)<br>www.meridanerealty.com</div>
  <div class="watermark" aria-hidden="true">MERIDANE</div>
  <div class="address-band">1840 W Larch Ave., Chicago, IL 60612</div>
</section>

<section class="sheet fax-cover">
  <div class="brand"><span class="brand-name">MERIDANE</span><span class="brand-sub">REALTY GROUP LLC</span></div>
  <div class="contact">312.555.0146<br>312.555.0147 (fax)<br>www.meridanerealty.com</div>
  <div class="fax-fields">
    <span>To</span><span></span><span>From</span><span></span>
    <span>Fax</span><span></span><span>Pages</span><span></span>
    <span>Re</span><span></span><span>Date</span><span></span>
  </div>
  <div class="fax-options">
    <label><i></i>Urgent</label>
    <label><i></i>For Review</label>
    <label><i></i>Please comment</label>
    <label><i></i>Please reply</label>
    <label><i></i>Please recycle</label>
  </div>
  <div class="fax-comments">Comments :</div>
  <div class="watermark" aria-hidden="true">MERIDANE</div>
  <div class="address-band">1840 W Larch Ave., Chicago, IL 60612</div>
</section>

<section class="card card-front">
  <div class="brand"><span class="brand-name">MERIDANE</span><span class="brand-sub">REALTY GROUP LLC</span></div>
  <div class="card-person">R. Paul Hensley, Esq<br>Managing Broker<br>hensley@meridanerealty.com</div>
  <div class="card-phones">312.555.0146<br>312.555.0147 (fax)</div>
  <div class="card-band">1840 W Larch Ave., Chicago, IL 60612</div>
</section>

<section class="card card-back">
  <div class="card-back-name" aria-hidden="true">MERIDANE</div>
  <div class="card-url">www.meridanerealty.com</div>
</section>

<section class="envelope envelope-front">
  <div class="brand"><span class="brand-name">MERIDANE</span><span class="brand-sub">REALTY GROUP LLC</span></div>
  <div class="watermark" aria-hidden="true">MERIDANE</div>
  <div class="address-band">1840 W Larch Ave., Chicago, IL 60612</div>
</section>

<section class="envelope envelope-back">
  <svg viewBox="0 0 307 135" aria-hidden="true">
    <path d="M0 0 L125 70 Q153 90 181 70 L307 0" fill="none" stroke="#cfd1d4" stroke-width="1.2"/>
    <path d="M0 135 L110 72 M307 135 L196 72" fill="none" stroke="#e2e3e5" stroke-width="1"/>
  </svg>
  <div class="envelope-mark" aria-hidden="true"></div>
  <div class="envelope-url">www.meridanerealty.com</div>
</section>

</body>
</html>
```